Snow & Ice Melter

We need a bag design for a new product our company is producing. Our company, Kelbrook Yardcare Products manufactures ice melt for melting snow. We are in the process of developing a new ice melt product called "Gumbo's Dreadwhirl snow & ice melter". We would like to see designs that include a logo for the product, a snowman (that depicts Gumbo) and a wintery background. To get an idea of our current product packaging go to our website at http://www.kelbrookyp.com

```html
<!DOCTYPE html>
<html lang="en">
<head>
<meta charset="utf-8">
<title>Gumbo's Dreadwhirl – Snow and Ice Melter</title>
<link rel="stylesheet" href="https://fonts.googleapis.com/css2?family=Poppins:wght@200;300&display=swap">
<style>
  :root {
    --sky-top: #5e5f62;
    --sky-mid: #4d6a75;
    --sky-bottom: #087b8e;
    --name-ink: #1b1b1c;
    --tagline-ink: #e9eff1;
    --drift-light: #c9cacc;
    --drift-dark: #7d7f82;
    --snowman-light: #ffffff;
    --snowman-shade: #c6c9cc;
  }
  html, body {
    margin: 0;
    padding: 0;
    overflow: hidden;
    background: var(--sky-top);
  }
  .banner {
    position: relative;
    width: 1200px;
    height: 499px;
    overflow: hidden;
    background: linear-gradient(180deg, var(--sky-top) 0%, var(--sky-mid) 50%, var(--sky-bottom) 100%);
  }
  .backdrop {
    position: absolute;
    inset: 0;
  }
  .product-name {
    position: absolute;
    left: 46px;
    top: 8px;
    margin: 0;
    font-family: "Poppins", sans-serif;
    font-weight: 300;
    font-size: 140px;
    line-height: 1.02;
    letter-spacing: -3px;
    color: var(--name-ink);
    white-space: nowrap;
  }
  .product-name span {
    display: block;
  }
  .tagline {
    position: absolute;
    left: 58px;
    top: 292px;
    margin: 0;
    font-family: "Poppins", sans-serif;
    font-weight: 200;
    font-size: 70px;
    line-height: 1;
    letter-spacing: -1px;
    color: var(--tagline-ink);
    white-space: nowrap;
  }
  .mascot {
    position: absolute;
    left: 822px;
    top: 76px;
    width: 335px;
    height: 423px;
  }
</style>
</head>
<body>
  <div class="banner">
    <svg class="backdrop" width="1200" height="499" viewBox="0 0 1200 499" aria-hidden="true">
      <defs>
        <linearGradient id="snowball" x1="0" y1="0" x2="0" y2="1">
          <stop offset="0" stop-color="#d9e1e4"/>
          <stop offset="1" stop-color="#3a8c9c"/>
        </linearGradient>
        <linearGradient id="drift" x1="0" y1="0" x2="0" y2="1">
          <stop offset="0" stop-color="var(--drift-dark)"/>
          <stop offset="1" stop-color="var(--drift-light)"/>
        </linearGradient>
      </defs>
      <g class="snowballs" fill="url(#snowball)">
        <circle cx="790" cy="44" r="10"/>
        <circle cx="1084" cy="28" r="10"/>
        <circle cx="22" cy="300" r="7"/>
        <circle cx="1060" cy="162" r="9"/>
        <circle cx="1098" cy="230" r="38"/>
        <circle cx="89" cy="404" r="14"/>
        <circle cx="434" cy="394" r="11"/>
        <circle cx="234" cy="450" r="10"/>
        <circle cx="623" cy="442" r="38"/>
        <circle cx="1189" cy="360" r="26"/>
        <circle cx="790" cy="335" r="3"/>
      </g>
      <path class="snow-drift" fill="url(#drift)"
        d="M0 482 C20 470 30 440 60 436 C120 430 200 440 260 434 C320 430 380 428 420 440
           C450 452 440 470 470 480 C500 488 520 470 560 456 C620 438 680 430 740 436
           C790 440 820 428 860 426 C920 424 980 440 1040 440 C1100 440 1130 430 1165 428
           C1185 428 1195 434 1200 440 L1200 499 L0 499 Z"/>
    </svg>

    <h1 class="product-name"><span>Gumbo’s</span><span>dreadwhirl</span></h1>
    <p class="tagline">snow and ice melter</p>

    <svg class="mascot" viewBox="0 0 335 423" role="img" aria-label="Illustration of Gumbo the worried snowman with twig arms">
      <defs>
        <radialGradient id="mascot-fill" cx="0.4" cy="0.4" r="0.7">
          <stop offset="0" stop-color="var(--snowman-light)"/>
          <stop offset="1" stop-color="var(--snowman-shade)"/>
        </radialGradient>
      </defs>
      <rect x="38" y="0" width="225" height="423" rx="110" fill="url(#mascot-fill)"/>
    </svg>
  </div>
</body>
</html>
```